Tech Company Letterhead/Business Cards/Envelopes

We would like a new stationary design for a technology company that develops full turnkey solutions for governments related to Data, Identity Tracking, Fingerprinting, Passport Control, and Border Protection Systems.

We would like the stationary designs to include:

Letter Head
Business Cards
Envelopes

Target Market(s)

Corporate

Industry/Entity Type

Business

Contact Information for Business Card

Details to be shared with the winner.

Font styles to use
Serif
Sans Serif

Colors
e4daeb
85abd2
3176b5
0355a3
0692cd

```html
<!DOCTYPE html>
<html lang="en">
<head>
<meta charset="utf-8">
<title>NEXID Stationery</title>
<link href="https://fonts.googleapis.com/css2?family=Montserrat:wght@400;500;600&display=swap" rel="stylesheet">
<style>
  :root {
    --brand-blue: #0873bd;
    --brand-grey: #545454;
    --faint-blue: #4f86c6;
    --paper: #ffffff;
    --backdrop: #dcdcdc;
    --text: #3a3a3a;
  }
  * { margin: 0; padding: 0; box-sizing: border-box; }
  html, body { width: 1200px; height: 1194px; overflow: hidden; }
  body {
    position: relative;
    background: var(--backdrop);
    font-family: "Montserrat", sans-serif;
    color: var(--text);
  }
  .piece { position: absolute; overflow: hidden; }
  .wordmark {
    position: absolute;
    font-weight: 600;
    color: var(--brand-blue);
    letter-spacing: 0.04em;
    line-height: 1;
    white-space: nowrap;
  }
  .band { position: absolute; left: 0; bottom: 0; display: block; }
  .contact-list { position: absolute; list-style: none; }
  .contact-list li { display: flex; align-items: center; gap: 6px; white-space: nowrap; }
  .contact-list svg { width: 7px; height: 7px; fill: none; stroke: var(--brand-blue); stroke-width: 1.6; flex: none; }
  .address { position: absolute; text-align: right; white-space: nowrap; letter-spacing: 0.02em; }

  /* Letterhead */
  .letterhead { left: 46px; top: 78px; width: 527px; height: 682px; background: var(--paper); }
  .letterhead .wordmark { left: 21px; top: 22px; font-size: 48px; }
  .letterhead .rule { position: absolute; left: 21px; top: 601px; width: 487px; height: 1px; background: var(--brand-blue); }
  .letterhead .contact-list { left: 21px; top: 609px; font-size: 10.5px; line-height: 13.2px; letter-spacing: 0.03em; }
  .letterhead .address { right: 20px; top: 618px; font-size: 10.5px; line-height: 13px; }

  /* Business card */
  .card { width: 381px; height: 218px; border-radius: 18px; }
  .card-front { left: 628px; top: 165px; background: var(--paper); }
  .card-front .wordmark { left: 21px; top: 24px; font-size: 40px; }
  .card-front .holder { position: absolute; right: 19px; top: 113px; text-align: right; }
  .card-front .holder-name { font-size: 14.5px; font-weight: 600; color: var(--brand-blue); letter-spacing: 0.02em; }
  .card-front .holder-role { font-size: 8.5px; letter-spacing: 0.04em; margin-top: 1px; }
  .card-front .rule { position: absolute; left: 21px; top: 145px; width: 341px; height: 1px; background: var(--brand-grey); }
  .card-front .contact-list { left: 21px; top: 155px; font-size: 9.2px; line-height: 12px; letter-spacing: 0.03em; }
  .card-front .address { right: 19px; top: 159px; font-size: 9.2px; line-height: 12px; }
  .card-back { left: 628px; top: 485px; background: var(--brand-blue); }
  .card-back .wordmark { left: 50%; top: 50%; transform: translate(-50%, -50%); font-size: 60px; color: var(--paper); }

  /* Envelopes */
  .envelope-front { left: 28px; top: 834px; width: 565px; height: 294px; }
  .envelope-front .flap { position: absolute; left: 0; top: 0; display: block; }
  .envelope-front .face { position: absolute; left: 0; top: 38px; width: 565px; height: 256px; background: var(--paper); overflow: hidden; }
  .envelope-front .wordmark { left: 50%; top: 88px; transform: translateX(-50%); font-size: 60px; }
  .envelope-front .address { right: 20px; top: 225px; font-size: 12px; line-height: 14.5px; color: var(--paper); }
  .envelope-back { left: 605px; top: 872px; width: 566px; height: 256px; background: var(--brand-blue); }
  .envelope-back .flap-edge { position: absolute; left: 0; top: 0; display: block; }
  .envelope-back .wordmark { left: 50%; top: 104px; transform: translateX(-50%); font-size: 86px; color: var(--faint-blue); }
  .envelope-back .web { position: absolute; left: 0; right: 0; top: 226px; text-align: center; font-size: 12.5px; color: var(--paper); letter-spacing: 0.04em; }
</style>
</head>
<body>

<svg width="0" height="0" style="position:absolute" aria-hidden="true">
  <defs>
    <symbol id="icon-phone" viewBox="0 0 10 10"><path d="M2 1 L4 3 L3 4.5 Q4.5 6.5 5.5 7 L7 6 L9 8 L7.5 9.3 Q3 8 0.8 2.5 Z"/></symbol>
    <symbol id="icon-landline" viewBox="0 0 10 10"><path d="M1 4 Q5 1 9 4 M2.5 5 H7.5 L8.5 9 H1.5 Z"/></symbol>
    <symbol id="icon-mail" viewBox="0 0 10 10"><rect x="1" y="2" width="8" height="6"/><path d="M1 2 L5 5.5 L9 2"/></symbol>
    <symbol id="icon-web" viewBox="0 0 10 10"><circle cx="5" cy="5" r="4"/><path d="M1 5 H9 M5 1 Q2.5 5 5 9 M5 1 Q7.5 5 5 9"/></symbol>
  </defs>
</svg>

<!-- Letterhead -->
<section class="piece letterhead" aria-label="Letterhead">
  <div class="wordmark">NEXID</div>
  <div class="rule"></div>
  <ul class="contact-list">
    <li><svg><use href="#icon-phone"/></svg>02 5550 1420</li>
    <li><svg><use href="#icon-landline"/></svg>1300 555 019</li>
    <li><svg><use href="#icon-mail"/></svg>info@nexid.com</li>
    <li><svg><use href="#icon-web"/></svg>www.NEXID.com</li>
  </ul>
  <div class="address">Level 4, 18 Harbour<br>Street Sydney 2000 NSW</div>
  <svg class="band" width="527" height="34" viewBox="0 0 527 34">
    <rect x="0" y="24" width="272" height="10" fill="var(--brand-grey)"/>
    <polygon points="301,0 527,0 527,34 265,34" fill="var(--brand-blue)"/>
  </svg>
</section>

<!-- Business card front -->
<section class="piece card card-front" aria-label="Business card front">
  <div class="wordmark">NEXID</div>
  <div class="holder">
    <div class="holder-name">Marcus Hale</div>
    <div class="holder-role">CEO &amp; Managing Director</div>
  </div>
  <div class="rule"></div>
  <ul class="contact-list">
    <li><svg><use href="#icon-phone"/></svg>02 5550 1420</li>
    <li><svg><use href="#icon-landline"/></svg>1300 555 019</li>
    <li><svg><use href="#icon-mail"/></svg>info@nexid.com</li>
    <li><svg><use href="#icon-web"/></svg>www.NEXID.com</li>
  </ul>
  <div class="address">Level 4, 18 Harbour<br>Street Sydney 2000 NSW</div>
  <svg class="band" width="381" height="25" viewBox="0 0 381 25">
    <rect x="0" y="17" width="197" height="8" fill="var(--brand-grey)"/>
    <polygon points="221,0 381,0 381,25 190,25" fill="var(--brand-blue)"/>
  </svg>
</section>

<!-- Business card back -->
<section class="piece card card-back" aria-label="Business card back">
  <div class="wordmark">NEXID</div>
</section>

<!-- Envelope front -->
<section class="piece envelope-front" aria-label="Envelope front">
  <svg class="flap" width="565" height="38" viewBox="0 0 565 38">
    <polygon points="36,0 528,0 565,38 0,38" fill="var(--brand-blue)"/>
  </svg>
  <div class="face">
    <div class="wordmark">NEXID</div>
    <svg class="band" width="565" height="38" viewBox="0 0 565 38">
      <rect x="0" y="26" width="293" height="12" fill="var(--brand-grey)"/>
      <polygon points="325,0 565,0 565,38 287,38" fill="var(--brand-blue)"/>
    </svg>
    <div class="address">Level 4, 18 Harbour<br>Street Sydney 2000 NSW</div>
  </div>
</section>

<!-- Envelope back -->
<section class="piece envelope-back" aria-label="Envelope back">
  <svg class="flap-edge" width="566" height="38" viewBox="0 0 566 38">
    <polygon points="0,0 566,0 527,38 39,38" fill="var(--paper)"/>
  </svg>
  <div class="wordmark">NEXID</div>
  <div class="web">www.NEXID.com</div>
</section>

</body>
</html>
```